Commercial and Residential Paint Contractor needs website

We need a website for our residential painting, multi-family painting and commercial painting company. We paint interior and exterior of houses, apartments and commercial buildings. I would like an about us page, residential page, multi family page, commercial page and contact us. Need keywords added to website for seo opitimazation. I like this website https://www.velmorandhalestudio.com/

Target Market(s)

General Contractors and commercial property managers

Coding

Coded - Design and coding required

Number of Pages Required

5+ page

Font styles to use
Sans Serif

Requirements
Must have
• I need SEO keywords on pages

```html
<!DOCTYPE html>
<html lang="en">
<head>
<meta charset="utf-8">
<title>Halden Painting – Residential &amp; Commercial Painting</title>
<link href="https://fonts.googleapis.com/css2?family=Mulish:wght@400;600;700;800&display=swap" rel="stylesheet">
<style>
:root{
  --red:#dc1f35;
  --blue:#1766b7;
  --navy:#1b3c7a;
  --ink:#1c1c1c;
  --white:#ffffff;
  --muted:#444a52;
}
*{margin:0;padding:0;box-sizing:border-box}
html,body{width:1200px;height:2458px;overflow:hidden;background:var(--white)}
body{position:relative;font-family:"Mulish",sans-serif;color:var(--ink)}
.abs{position:absolute}

/* header */
.site-header{left:0;top:0;width:1200px;height:53px;background:var(--white)}
.brand{left:242px;top:12px;font-weight:800;font-size:26px;letter-spacing:1px;color:var(--navy);line-height:30px}
.main-nav{left:487px;top:0;height:53px;display:flex;gap:25px;font-size:9px;font-weight:700;letter-spacing:.8px}
.main-nav a{color:var(--ink);text-decoration:none;line-height:53px;position:relative}
.main-nav a.active::after{content:"";position:absolute;left:-6px;right:-6px;bottom:0;height:3px;background:var(--red)}
.call-btn{left:922px;top:16px;width:121px;height:26px;border-radius:13px;background:var(--blue);color:var(--white);font-size:10px;font-weight:700;display:flex;align-items:center;justify-content:center;gap:6px}

/* hero */
.hero{left:0;top:53px;width:1200px;height:462px;background:linear-gradient(90deg,#b9b07c 0%,#c9c8bd 22%,#8a97a8 45%,#7d8a9c 70%,#97a3b2 100%)}
.hero-floor{left:0;top:420px;width:1200px;height:95px;background:linear-gradient(180deg,rgba(190,195,202,0) 0%,#aeb4bb 100%)}
.hero-title{left:0;top:195px;width:1200px;text-align:center;color:var(--white);font-weight:800;font-size:38px;line-height:46px}
.hero-sub{left:0;top:298px;width:1200px;text-align:center;color:var(--white);font-size:8.5px;font-weight:600;letter-spacing:1.2px}
.hero-btn{left:535px;top:326px;width:122px;height:29px;background:var(--red);color:var(--white);font-size:8.5px;font-weight:700;display:flex;align-items:center;justify-content:center}

/* about band */
.about-band{left:0;top:515px;width:1200px;height:366px;background:var(--red)}
.about-title{left:242px;top:570px;width:380px;color:var(--white);font-weight:800;font-size:29px;line-height:36px;white-space:nowrap}
.about-text{left:629px;top:578px;width:345px;color:var(--white);font-size:13px;line-height:18.8px}
.dial-box{left:365px;top:768px;width:469px;height:50px;border:2px solid var(--white);border-radius:10px;color:var(--white);font-size:12.5px;font-weight:600;display:flex;align-items:center;justify-content:center}

/* services */
.service-photo{top:987px;width:347px;height:318px;border-radius:3px}
.service-res{left:242px;background:linear-gradient(180deg,#7ea3cf 0%,#b9a893 45%,#6d6a68 75%,#5a5d62 100%)}
.service-com{left:607px;background:linear-gradient(180deg,#d9dde2 0%,#3e5fae 45%,#3a5aa4 70%,#9b9a95 100%)}
.service-caption{top:1325px;width:347px;text-align:center;font-weight:800;font-size:21px;line-height:27px}
.service-caption .accent-red{color:var(--red)}
.service-caption .accent-blue{color:var(--blue)}

/* featured projects */
.featured-block{left:0;top:1462px;width:251px;height:263px;background:var(--red)}
.featured-title{left:47px;top:1508px;color:var(--white);font-weight:800;font-size:38px;line-height:42px}
.view-all{left:47px;top:1661px;width:103px;height:29px;background:var(--white);color:var(--ink);font-size:9px;font-weight:800;letter-spacing:.6px;display:flex;align-items:center;justify-content:center}
.project{top:1462px;height:263px}
.project-gym{left:259px;width:285px;background:linear-gradient(180deg,#2a2c31 0%,#47536b 45%,#6f7175 100%)}
.project-lobby{left:550px;width:321px;background:linear-gradient(90deg,#d7d6d1 0%,#f0efec 45%,#5b5b5b 85%,#aaa9a5 100%)}
.project-house{left:880px;width:320px;background:linear-gradient(180deg,#4d82c8 0%,#5e5a55 45%,#6f8a5a 80%,#8e9a72 100%)}

/* quote */
.quote{left:0;top:1774px;width:1200px;text-align:center;font-size:22px;font-weight:600}
.quote .num{color:var(--red);margin-left:6px}
.quote-sub{left:0;top:1815px;width:1200px;text-align:center;font-size:12px;font-weight:600;letter-spacing:.3px}

/* interior banner */
.interior{left:0;top:1873px;width:1200px;height:336px;background:linear-gradient(90deg,#e4e1dc 0%,#f6f4f0 30%,#ecebe8 60%,#e7e3e0 100%)}
.interior-floor{left:0;top:2110px;width:1200px;height:99px;background:linear-gradient(180deg,rgba(205,203,200,0) 0%,#c9c6c1 100%)}

/* footer */
.site-footer{left:0;top:2209px;width:1200px;height:201px;background:var(--blue)}
.foot-contact{left:215px;top:2264px;width:280px;text-align:center;color:var(--white);font-size:9.5px;letter-spacing:.8px;line-height:17px;white-space:nowrap}
.foot-btn{left:303px;top:2329px;width:105px;height:26px;border:1.5px solid var(--white);border-radius:13px;color:var(--white);font-size:10.5px;display:flex;align-items:center;justify-content:center}
.foot-brand{left:500px;top:2262px;width:200px;text-align:center;color:var(--white);font-weight:800;font-size:20px;letter-spacing:1px}
.foot-about{left:485px;top:2300px;width:230px;text-align:center;color:var(--white);font-size:9.3px;line-height:15px}
.social{top:2295px;width:32px;height:32px;border-radius:50%;background:#0f1a2b}
.copyright{left:0;top:2434px;width:1200px;text-align:center;font-size:9.5px;letter-spacing:.8px;color:var(--muted)}
</style>
</head>
<body>

<header class="abs site-header">
  <div class="abs brand">HALDEN</div>
  <nav class="abs main-nav">
    <a href="#" class="active">HOME</a>
    <a href="#">ABOUT US</a>
    <a href="#">RESIDENTIAL</a>
    <a href="#">COMMERCIAL</a>
    <a href="#">CONTACT US</a>
  </nav>
  <div class="abs call-btn">
    <svg width="12" height="12" viewBox="0 0 24 24" fill="none" stroke="#fff" stroke-width="2"><path d="M5 3h4l2 5-2.5 1.5a11 11 0 0 0 6 6L16 13l5 2v4a2 2 0 0 1-2 2A17 17 0 0 1 3 5a2 2 0 0 1 2-2z"/></svg>
    800 555 0142
  </div>
</header>

<section>
  <div class="abs hero" role="img" aria-label="Bright living room with grey sofa, rug, coffee table and garden view through tall windows"></div>
  <div class="abs hero-floor"></div>
  <h1 class="abs hero-title">Top quality paintings<br>by top quality painters</h1>
  <p class="abs hero-sub">HALDEN PAINTING PERFORMS INTERIOR AND EXTERIOR PAINTINGS.</p>
  <div class="abs hero-btn">CONTACT US TODAY</div>
</section>

<section class="abs about-band"></section>
<h2 class="abs about-title">Halden Painting - We are<br>family owned and<br>operated with over 10<br>years’ experience.</h2>
<p class="abs about-text">We pride our self in performing to the highest degree of workmanship standards. Halden Painting is your best choice for commercial, residential and multi-family painting in the DFW/Forth Worth area. Our experienced estimators will meet with you and customize a proposal to meet your needs. They will stay with you from the beginning of the project to the end, making sure you are 100% satisfied.</p>
<div class="abs dial-box">If you are looking for a dependable painter call our office 972-555-0188</div>

<section>
  <div class="abs service-photo service-res" role="img" aria-label="Modern two-storey house with wood cladding and grey garage door"></div>
  <div class="abs service-photo service-com" role="img" aria-label="Blue corrugated commercial warehouse building with loading door"></div>
  <h3 class="abs service-caption" style="left:242px">Exterior &amp; Interior<br><span class="accent-red">Residential</span> Painting service</h3>
  <h3 class="abs service-caption" style="left:607px">Exterior &amp; Interior<br><span class="accent-blue">Commercial</span> Painting service</h3>
</section>

<section>
  <div class="abs featured-block"></div>
  <h2 class="abs featured-title">Our<br>featured<br>projects</h2>
  <div class="abs view-all">VIEW ALL</div>
  <div class="abs project project-gym" role="img" aria-label="Gym interior with a printed feature wall and training mats"></div>
  <div class="abs project project-lobby" role="img" aria-label="Tall white lobby with stone accent wall and lounge chairs"></div>
  <div class="abs project project-house" role="img" aria-label="Painted family home with blue siding and white porch"></div>
</section>

<p class="abs quote">For a free quote , please call us at <span class="num">(972)-555-0188</span></p>
<p class="abs quote-sub">We promise, you won’t be dissapointed</p>

<div class="abs interior" role="img" aria-label="Freshly painted white open-plan apartment with kitchen, mirror and patterned rug"></div>
<div class="abs interior-floor"></div>

<footer class="abs site-footer"></footer>
<div class="abs foot-contact">TEL: 972-555-0188<br>E-MAIL: INFO@HALDENPAINTING.COM<br>4810 CEDAR LANE</div>
<div class="abs foot-btn">Contact Us</div>
<div class="abs foot-brand">HALDEN</div>
<p class="abs foot-about">Halden Painting Company is a full service painting company. We are proud to offer superior customer service and professional workmanship.</p>
<div class="abs social" style="left:787px" aria-label="Social profile"></div>
<div class="abs social" style="left:826px" aria-label="Social profile"></div>
<div class="abs social" style="left:865px" aria-label="Social profile"></div>

<p class="abs copyright">HALDEN PAINTING © 2020. ALL RIGHTS RESERVED.</p>

</body>
</html>
```